I need a logo design for a new company based in Tucson called "Mindpilot Reg Holloway". I am a psychotherapist that specializes in clinical psychology with athletes and performers. The final design should incorporate the psychology symbol as a watermark. The logo should convey movement and fluidity. "Mindpilot" is a bit of a play on words combining psychology (head) with sports (coach). Other design interests include mid-century, Ansel Brigham Kotter. I will want to use the logo for business cards, letterhead and marketing brochures. I will put together a website at a later date. I am attaching a file with some pertinent information for the business card. Thank you.
Reg Holloway
mindpilotregholloway@quillmarsh.net
Updates

Thank you all for the submissions so far.  I have submitted an additional file with a draft of a new design idea.  Since "mindpilot" is a bit of a play on words, I would like to see something with the two "H's" look something like quotation marks.  If the psychology logo is to be included at all, it needs to be less prominent.     Thank you all.  Reg                               

Target Market(s)

1) Adolescent and adult athletes and performers who are looking to increase their level of performance (Sport and Performance Psychology)
2) Adult psychotherapy patients (Clinical psychology)

Industry/Entity Type

Marketing

Colors

Designer to choose colors to be used in the design.

Requirements
Must have
• 1) Since "mindpilot" is a bit of a play on words, The "H's" need to be in a font that looks somewhat like quotation marks.

Nice to have
• Logo on one side. All other info on the backside?

```html
<!DOCTYPE html>
<html lang="en">
<head>
<meta charset="utf-8">
<title>Mindpilot Reg Holloway – Business Card</title>
<link href="https://fonts.googleapis.com/css2?family=Didact+Gothic&display=swap" rel="stylesheet">
<style>
  :root {
    --page-bg: #eceae6;
    --navy: #0c3a6b;
    --ocean: #2f7cc0;
    --sky: #6aa6dc;
    --ink-blue: #2b3f9a;
    --accent-orange: #e8651f;
    --card-white: #ffffff;
    --watermark: #e3e3e3;
    --muted-blue: #3a5a9c;
  }
  * { box-sizing: border-box; margin: 0; padding: 0; }
  html, body {
    width: 1200px;
    height: 784px;
    overflow: hidden;
    background: var(--page-bg);
    font-family: "Didact Gothic", "Century Gothic", sans-serif;
  }
  .card-set {
    position: absolute;
    inset: 0;
    display: flex;
    align-items: center;
    justify-content: center;
    gap: 40px;
  }
  .card {
    position: relative;
    width: 540px;
    height: 309px;
    overflow: hidden;
    box-shadow: 0 6px 18px rgba(0,0,0,0.15);
  }

  /* Front */
  .card-front { background: var(--navy); }
  .front-pattern {
    position: absolute;
    inset: 0;
    background:
      radial-gradient(ellipse at 85% 20%, rgba(106,166,220,0.55), transparent 60%),
      linear-gradient(135deg, var(--navy) 0%, var(--ocean) 55%, var(--sky) 100%);
  }
  .front-wordmark {
    position: absolute;
    left: 0;
    right: 0;
    top: 118px;
    text-align: center;
    color: var(--card-white);
    font-size: 42px;
    line-height: 1;
  }
  .front-wordmark .subname {
    display: block;
    margin-top: 10px;
    font-size: 22px;
    letter-spacing: 4px;
  }

  /* Back */
  .card-back { background: var(--card-white); }
  .psi-watermark {
    position: absolute;
    right: 22px;
    top: 10px;
    font-size: 250px;
    line-height: 1;
    color: var(--watermark);
  }
  .back-wordmark {
    position: absolute;
    left: 44px;
    top: 40px;
    color: var(--ink-blue);
    font-size: 34px;
    line-height: 1;
  }
  .back-wordmark .subname {
    display: block;
    margin-top: 6px;
    margin-left: 40px;
    font-size: 18px;
    letter-spacing: 3px;
  }
  .identity {
    position: absolute;
    left: 44px;
    top: 160px;
  }
  .person-name {
    color: var(--accent-orange);
    font-size: 22px;
    font-weight: 700;
  }
  .person-role {
    color: var(--muted-blue);
    font-size: 13px;
    margin-top: 2px;
  }
  .contact-list {
    list-style: none;
    margin-top: 10px;
  }
  .contact-list li {
    display: flex;
    align-items: center;
    gap: 8px;
    color: var(--ink-blue);
    font-size: 16px;
    line-height: 23px;
  }
  .contact-icon {
    width: 15px;
    height: 15px;
    flex: none;
    fill: var(--accent-orange);
    stroke: var(--accent-orange);
  }
</style>
</head>
<body>
  <main class="card-set">
    <section class="card card-front" aria-label="Card front">
      <div class="front-pattern" role="img" aria-label="Blue field of overlapping light ovals receding in perspective"></div>
      <div class="front-wordmark">Mindpilot<span class="subname">Reg Holloway</span></div>
    </section>

    <section class="card card-back" aria-label="Card back">
      <div class="psi-watermark" aria-hidden="true">Ψ</div>
      <div class="back-wordmark">Mindpilot<span class="subname">Reg Holloway</span></div>
      <div class="identity">
        <p class="person-name">Reg Holloway</p>
        <p class="person-role">Psychologist</p>
        <ul class="contact-list">
          <li>
            <svg class="contact-icon" viewBox="0 0 16 16" aria-hidden="true"><path stroke="none" d="M3 1.5l3 .5 1 3.5-2 1.3a8 8 0 0 0 4.2 4.2L10.5 9l3.5 1 .5 3-2 1.5C6.5 14 2 9.5 1.5 3.5z"/></svg>
            1520 381 276
          </li>
          <li>
            <svg class="contact-icon" viewBox="0 0 16 16" aria-hidden="true"><path stroke="none" d="M8 1.5L1 8h2v6.5h4V10h2v4.5h4V8h2z"/></svg>
            PO Box 47190 AZ 85719
          </li>
          <li>
            <svg class="contact-icon" viewBox="0 0 16 16" aria-hidden="true"><rect x="1.5" y="3.5" width="13" height="9" fill="none" stroke-width="1.6"/><path d="M1.5 3.5L8 9l6.5-5.5" fill="none" stroke-width="1.6"/></svg>
            mindpilotregholloway@quillmarsh.net
          </li>
          <li>
            <svg class="contact-icon" viewBox="0 0 16 16" aria-hidden="true"><g fill="none" stroke-width="1.3"><circle cx="8" cy="8" r="6.5"/><ellipse cx="8" cy="8" rx="3" ry="6.5"/><path d="M1.5 8h13M2.5 4.8h11M2.5 11.2h11"/></g></svg>
            www.mindpilotregholloway.com
          </li>
        </ul>
      </div>
    </section>
  </main>
</body>
</html>
```